Business website cyber security

Full redesign of our current business website, mockup and powerpoint presentation have been provided.
Some animated elements (example: SVG with CSS) are welcome.
A detailed requirement list can also be found in the attached powerpoint
Also uploaded is the current page as a nicepage & html export. All 11 sites shall be reworked. "Branches", "Download", "Contact" and "Legal Information" are not needed .

A good example of a competitor is https://www.fennotrix.de/ this. Not in terms of colors, but in regard to website structure, animated elements and overall look.

Target Market(s)

Cyber security for the B2B market

Industry/Entity Type

IT, IT Security, banking

Coding

Coded - Design and coding required

Number of Pages Required

5+ page

Other font styles liked:
• ReadexPro Regular, ReadexPro Light

Colors
0054AA
0677BA
7BADD7
CADEEF
E8F1F8

Requirements
Must have
• Modern and sleek design, corporate identity
Nice to have
• Animated elements (css svg)
Should not have
• too many colors (max 4), too fancy

```html
<!DOCTYPE html>
<html lang="de">
<head>
<meta charset="utf-8">
<title>Vextra – IT · Security · Compliance</title>
<link href="https://fonts.googleapis.com/css2?family=Lexend:wght@300;400;500;600;700&display=swap" rel="stylesheet">
<style>
:root{
  --navy-900:#061a36;
  --navy-800:#08213f;
  --navy-700:#0c3a69;
  --navy-600:#0d4477;
  --brand:#0054aa;
  --brand-2:#0677ba;
  --accent:#3d8fe0;
  --sky:#7badd7;
  --panel:#b3d4fb;
  --ice:#e8f1f8;
  --white:#ffffff;
  --ink:#0a2545;
}
*{margin:0;padding:0;box-sizing:border-box}
html,body{width:1200px;height:2202px;overflow:hidden}
body{
  position:relative;
  font-family:'Lexend',sans-serif;
  color:var(--white);
  background:linear-gradient(180deg,var(--navy-900) 0%,var(--navy-800) 45%,#0a3666 80%,#0b4a82 100%);
}
.abs{position:absolute}

/* header */
.site-header{left:0;top:0;width:1200px;height:88px;background:var(--navy-600)}
.brand{display:flex;align-items:center;gap:10px;left:89px;top:28px;font-weight:600;font-size:24px;color:var(--white)}
.brand-dot{width:26px;height:26px;border-radius:50%;background:var(--white)}
.nav-link{top:34px;font-size:14px;font-weight:500;color:var(--white)}
.nav-link.active{text-decoration:underline;text-underline-offset:5px}
.flag{left:1080px;top:34px;width:32px;height:21px;display:flex;flex-direction:column}
.flag span{flex:1}

/* hero */
.hero-visual{left:584px;top:88px;width:616px;height:492px;
  clip-path:polygon(56px 0,100% 0,100% 100%,0 100%);
  background:radial-gradient(circle at 45% 55%,#1fb6ff 0%,#0d6fd0 30%,#0a3f9a 60%,#071f55 100%)}
.hero-title{left:88px;top:229px;width:480px;font-size:38px;line-height:42px;font-weight:700;color:var(--accent);letter-spacing:.5px}
.hero-text{left:88px;top:386px;width:450px;font-size:14.5px;line-height:21.7px;font-weight:400}

/* service cards */
.service-card{top:661px;width:325px;height:178px;background:var(--navy-700);border-radius:3px}
.service-card svg{position:absolute;left:27px;top:60px}
.service-card h3{position:absolute;left:111px;top:20px;width:200px;font-size:17px;line-height:22px;font-weight:600;color:var(--accent)}
.service-card p{position:absolute;left:111px;width:200px;font-size:12.6px;line-height:17.5px;font-weight:400}

/* section titles */
.section-title{left:0;width:1200px;text-align:center;font-size:33px;font-weight:600;letter-spacing:.5px}
.section-sub{left:0;width:1200px;text-align:center;font-size:12.5px}

/* tabs */
.tab{left:148px;width:152px;height:52px;display:flex;align-items:center;justify-content:center;font-size:16px;font-weight:400;background:var(--brand);border-radius:2px}
.tab.current{background:var(--navy-700)}
.tab-panel{left:316px;top:985px;width:728px;height:319px;background:var(--panel);border-radius:2px;color:var(--ink);padding:30px 66px 0 33px}
.tab-panel::before{content:"";position:absolute;left:-10px;top:18px;border:10px solid transparent;border-left:0;border-right-color:var(--panel)}
.tab-panel h4{font-size:19.5px;font-weight:600;color:#0b3b7a;margin-bottom:10px;letter-spacing:.3px}
.tab-panel p,.tab-panel li{font-size:14px;line-height:19.3px}
.tab-panel .lead-in{color:#0b3b7a;font-weight:600;margin:16px 0 8px}
.tab-panel ul{list-style:none;margin-bottom:16px}

/* sector tiles */
.sector{width:325px;height:195px;border-radius:4px;overflow:hidden}
.sector .label{position:absolute;left:0;bottom:12px;width:100%;text-align:center;font-size:16px;font-weight:500}
.sector .shade{position:absolute;inset:0;background:linear-gradient(180deg,transparent 55%,rgba(0,0,0,.55))}
.ops{background:linear-gradient(180deg,#0b2c4e 0%,#041424 70%,#02080f 100%)}
.ops h5{position:absolute;left:70px;top:32px;font-size:24px;font-weight:600;letter-spacing:.5px}
.ops ul{position:absolute;left:70px;top:73px;list-style:none;font-size:14px;line-height:25px;font-weight:500}
.ops li::before{content:"";display:inline-block;border:4px solid transparent;border-left:5px solid var(--white);border-right:0;margin-right:6px}
.btn{position:absolute;left:68px;top:133px;width:98px;height:28px;background:var(--brand);border-radius:2px;font-size:12.5px;display:flex;align-items:center;justify-content:center}

/* footer */
.site-footer{left:0;top:1970px;width:1200px;height:190px;background:#0b4a82}
.footer-brand{display:flex;align-items:center;gap:12px;left:89px;top:2052px;font-size:28px;font-weight:600}
.footer-brand .brand-dot{width:34px;height:34px}
.footer-meta{left:0;top:2041px;width:1200px;text-align:center;font-size:13px;color:#3d9ae8}
.footer-link{top:2070px;font-size:14.5px}
.footer-link.active{text-decoration:underline;text-underline-offset:4px}
.social{left:1070px;top:2041px;width:41px;height:41px;border-radius:50%;background:var(--white)}
.copyright-bar{left:0;top:2160px;width:1200px;height:42px;background:#07264a;display:flex;align-items:center;justify-content:center;font-size:12.5px}

@keyframes pulse{0%,100%{opacity:.85}50%{opacity:1}}
.hero-visual{animation:pulse 4s ease-in-out infinite}
</style>
</head>
<body>

<header class="abs site-header"></header>
<div class="abs brand"><span class="brand-dot"></span>Vextra</div>
<nav>
  <a class="abs nav-link active" style="left:236px">CDaaS</a>
  <a class="abs nav-link" style="left:323px">Security Services</a>
  <a class="abs nav-link" style="left:482px">Compliance</a>
  <a class="abs nav-link" style="left:786px">Company</a>
  <a class="abs nav-link" style="left:892px">Career</a>
  <a class="abs nav-link" style="left:979px">Contact</a>
</nav>
<div class="abs flag" aria-label="Deutsch"><span style="background:#000"></span><span style="background:#dd0000"></span><span style="background:#ffce00"></span></div>

<section>
  <div class="abs hero-visual" role="img" aria-label="Isometric illustration of a secured laptop with shield, lock and gears in glowing blue"></div>
  <h1 class="abs hero-title">Die IT-Sicherheit Ihrer IT-Infrastruktur ist unsere Mission.</h1>
  <p class="abs hero-text">Unsere Cybersicherheitsdienste sind rund um den Kunden konzipiert. Wir bieten eine robuste Zusammenarbeit, um die Herausforderungen Ihrer Umgebung zu verstehen und maßgeschneiderte, sichere Lösungen zu entwickeln.</p>
</section>

<section>
  <article class="abs service-card" style="left:88px">
    <svg width="58" height="58" viewBox="0 0 58 58" fill="none" stroke="#7badd7" stroke-width="2.2">
      <path d="M29 8 L46 16 V30 C46 41 38 48 29 51 C20 48 12 41 12 30 V16 Z"/>
      <rect x="22" y="27" width="14" height="11" rx="1.5"/><path d="M25 27 v-4 a4 4 0 0 1 8 0 v4"/>
      <circle cx="6" cy="10" r="3.5"/><circle cx="52" cy="10" r="3.5"/><circle cx="6" cy="48" r="3.5"/><circle cx="52" cy="48" r="3.5"/>
      <path d="M9 12 L13 16 M49 12 L45 16 M9 46 L14 42 M49 46 L44 42"/>
    </svg>
    <h3>CDaas-Cyber Defense as a Service</h3>
    <p style="top:70px">Our all-in-one CDaaS offer offers a convenient integration of your IT infrastructure into an active and comprehensive security solution.</p>
  </article>
  <article class="abs service-card" style="left:437px">
    <svg width="58" height="66" viewBox="0 0 58 66" fill="none" stroke="#7badd7" stroke-width="2.2">
      <path d="M34 4 L52 11 V24 C52 35 44 42 34 45 C24 42 16 35 16 24 V11 Z"/>
      <path d="M26 23 L32 29 L43 17"/>
      <path d="M4 52 H18 L28 47 C32 45 35 49 31 51 L22 56 H36 L48 48 C51 46 54 50 51 52 L38 62 H4"/>
    </svg>
    <h3 style="top:22px">Security Services</h3>
    <p style="top:54px">Our security services provide you with comprehensive support in the planning and implementation of your ho-listic IT and information management.</p>
  </article>
  <article class="abs service-card" style="left:786px">
    <svg width="58" height="58" viewBox="0 0 58 58" fill="none" stroke="#7badd7" stroke-width="2.2">
      <rect x="6" y="4" width="36" height="48" rx="2"/>
      <path d="M12 16 l3 3 5-6 M24 16 H36 M12 28 l3 3 5-6 M24 28 H34 M12 40 l3 3 5-6 M24 40 H30"/>
      <circle cx="44" cy="44" r="9"/><path d="M40 44 l3 3 5-6"/>
    </svg>
    <h3 style="top:22px">Compliance</h3>
    <p style="top:52px">We support you with your IT security at the highest level with an effective compliance strategy.</p>
  </article>
</section>

<section>
  <h2 class="abs section-title" style="top:911px">Vision &amp; Mission</h2>
  <div class="abs tab current" style="top:983px">Vision</div>
  <div class="abs tab" style="top:1044px">Mission</div>
  <div class="abs tab" style="top:1105px">Portfolio</div>
  <div class="abs tab-panel">
    <h4>Holistic IT security is our claim.</h4>
    <p>We stand for your IT security. We offer extensive services and our certified IT experts work with you to ensure that your systems are secure.</p>
    <p class="lead-in">With us you have:</p>
    <ul>
      <li>• Fastest response times 24x7</li>
      <li>• Market<br>leading technologies</li>
      <li>• Certified cyber analysts with the highest level of expertise</li>
    </ul>
    <p>The "Pay-As-You-Grow" model allows ongoing adjustments to the professional security services used - with one claim: your needs.</p>
  </div>
</section>

<section>
  <h2 class="abs section-title" style="top:1374px">Industry Sectors</h2>
  <p class="abs section-sub" style="top:1421px">Sample text. Click to select the text box. Click again or double click to start editing the text.</p>

  <div class="abs sector" style="left:88px;top:1474px;background:linear-gradient(135deg,#5d7f9c,#2c4d6b 55%,#17324c)" role="img" aria-label="Photo of a hand with financial service icons"><div class="shade"></div><span class="label">Financial Sector</span></div>
  <div class="abs sector ops" style="left:438px;top:1474px">
    <h5>It Service OPS</h5>
    <ul><li>Event Management</li><li>Incident Management</li></ul>
    <span class="btn">Read More</span>
  </div>
  <div class="abs sector" style="left:787px;top:1474px;background:linear-gradient(135deg,#3e5e7d,#1c3650 60%,#0e1e30)" role="img" aria-label="Photo of engineers at monitors showing car designs"><div class="shade"></div><span class="label">Automobil Industrie</span></div>

  <div class="abs sector" style="left:88px;top:1694px;background:linear-gradient(160deg,#c69a5a,#7a7c86 45%,#2f3d55)" role="img" aria-label="Photo of wind turbines and solar panels at sunset"><div class="shade"></div><span class="label">Energy</span></div>
  <div class="abs sector" style="left:438px;top:1694px;background:linear-gradient(135deg,#2b4058,#5a88a6 55%,#1a2c40)" role="img" aria-label="Photo of a person holding a tablet with logistics icons"><div class="shade"></div><span class="label">Logistics</span></div>
  <div class="abs sector" style="left:787px;top:1694px;background:linear-gradient(135deg,#4a4338,#8a8578 55%,#2a2824)" role="img" aria-label="Photo of scales of justice on a desk"><div class="shade"></div><span class="label">Governorate</span></div>
</section>

<footer>
  <div class="abs site-footer"></div>
  <div class="abs footer-brand"><span class="brand-dot"></span>Vextra</div>
  <p class="abs footer-meta">© Vextra (S.à rl) • Tel.: +352 4180 27 31 - 10</p>
  <a class="abs footer-link active" style="left:415px">Contact</a>
  <a class="abs footer-link" style="left:509px">Imprint</a>
  <a class="abs footer-link" style="left:603px">Privacy</a>
  <a class="abs footer-link" style="left:695px">Legal Notice</a>
  <span class="abs social" aria-label="Social profile"></span>
  <div class="abs copyright-bar">Copyright © 2022 Vextra. All Rights Reserved</div>
</footer>

</body>
</html>
```